I want to revise my business card design and get a more modern and up to date design.

Brolvane Handyman Sevices originated from a family-owned and operated contractor business, performing home renovation, addition, and construction work in the NYC area since 2004. Today, we specialize in reliable and affordable handyman services for residential and commercial clients In 2014, we expanded to northern New Jersey. In 2016, we brought quality home improvement and repair services to new Bucks County, PA, and nearby New Jersey areas.
Target Market(s)
Home owners and business that might be looking for a General contractor, handyman, cleaning services and Home maintenance and property.
Industry/Entity Type
Construction Company
Contact Information for Business Card
I am open to new ideas
Colors
Designer to choose colors to be used in the design.
Look and feel
Each slider illustrates characteristics of the customer's brand and the style your logo design should communicate.

```html
<!DOCTYPE html>
<html lang="en">
<head>
<meta charset="utf-8">
<title>Brolvane Handyman Sevices – Business Card</title>
<link rel="stylesheet" href="https://fonts.googleapis.com/css2?family=Poppins:wght@400;500;700&display=swap">
<style>
  :root {
    --backdrop: #2b2b2b;
    --card: #262626;
    --red: #e5232a;
    --gold: #c9a227;
    --white: #f2f2f2;
    --muted: #cfcfcf;
  }
  * { box-sizing: border-box; margin: 0; padding: 0; }
  html, body {
    width: 1200px; height: 1200px; overflow: hidden;
    background: var(--backdrop);
    font-family: "Poppins", sans-serif;
  }
  .canvas {
    width: 1200px; height: 1200px;
    display: flex; flex-direction: column; align-items: center;
    justify-content: center; gap: 74px;
  }
  .card {
    width: 880px; height: 503px;
    background: var(--card);
    border-bottom: 7px solid var(--red);
    box-shadow: 0 14px 30px rgba(0,0,0,.45);
    position: relative;
  }
  .brand {
    display: flex; align-items: center; gap: 22px;
  }
  .brand-dot {
    width: 64px; height: 64px; border-radius: 50%;
    background: var(--red); flex: none;
  }
  .brand-name {
    color: var(--red); font-weight: 700;
    font-size: 40px; line-height: 1.1;
  }
  /* contact side */
  .card-contact {
    display: flex; align-items: center; padding: 0 70px;
  }
  .card-contact .brand-name { font-size: 34px; }
  .divider {
    width: 2px; height: 190px; background: var(--gold);
    margin: 0 44px 0 40px; flex: none;
  }
  .person-name {
    color: var(--red); font-weight: 700; font-size: 26px;
    letter-spacing: .5px; text-transform: uppercase;
  }
  .person-title {
    color: var(--white); font-size: 17px; margin-bottom: 20px;
  }
  .contact-list { list-style: none; }
  .contact-list li {
    display: flex; align-items: center; gap: 14px;
    color: var(--white); font-size: 18px; margin-bottom: 8px;
  }
  .contact-list svg { width: 18px; height: 18px; flex: none; }
  /* front side */
  .card-front {
    display: flex; flex-direction: column; align-items: center;
    justify-content: center; gap: 64px;
  }
  .card-front .brand-name { font-size: 48px; }
  .card-front .brand-dot { width: 80px; height: 80px; }
  .services {
    text-align: center; color: var(--white);
    font-size: 21px; font-weight: 500; line-height: 1.75;
  }
  .services .sep {
    display: inline-block; width: 9px; height: 9px;
    background: var(--white); margin: 0 8px 3px;
  }
</style>
</head>
<body>
<main class="canvas">
  <section class="card card-contact">
    <div class="brand">
      <span class="brand-dot"></span>
      <span class="brand-name">Brolvane<br>Handyman Sevices</span>
    </div>
    <span class="divider"></span>
    <div class="contact">
      <p class="person-name">Dario Mendel</p>
      <p class="person-title">Senior Consultant</p>
      <ul class="contact-list">
        <li>
          <svg viewBox="0 0 24 24" aria-hidden="true"><path fill="var(--red)" d="M6.6 10.8a15.1 15.1 0 0 0 6.6 6.6l2.2-2.2a1 1 0 0 1 1-.25 11.4 11.4 0 0 0 3.6.57 1 1 0 0 1 1 1V20a1 1 0 0 1-1 1A17 17 0 0 1 3 4a1 1 0 0 1 1-1h3.5a1 1 0 0 1 1 1c0 1.25.2 2.45.57 3.57a1 1 0 0 1-.25 1z"/></svg>
          (402) 555-0148
        </li>
        <li>
          <svg viewBox="0 0 24 24" aria-hidden="true"><rect x="2.5" y="5" width="19" height="14" rx="1.5" fill="none" stroke="var(--red)" stroke-width="2"/><path d="M3 6l9 7 9-7" fill="none" stroke="var(--red)" stroke-width="2"/></svg>
          brolvanehandyman@mail.com
        </li>
        <li>
          <svg viewBox="0 0 24 24" aria-hidden="true"><circle cx="12" cy="12" r="9.5" fill="none" stroke="var(--red)" stroke-width="2"/><ellipse cx="12" cy="12" rx="4" ry="9.5" fill="none" stroke="var(--red)" stroke-width="1.6"/><path d="M2.5 12h19" stroke="var(--red)" stroke-width="1.6"/></svg>
          www.brolvanehandyman.com
        </li>
      </ul>
    </div>
  </section>

  <section class="card card-front">
    <div class="brand">
      <span class="brand-dot"></span>
      <span class="brand-name">Brolvane<br>Handyman Sevices</span>
    </div>
    <p class="services">
      <span class="sep"></span>Commercial and Residential Contractor<br>
      <span class="sep"></span>Handyman <span class="sep"></span>Technician <span class="sep"></span>Repair <span class="sep"></span>Inprove <span class="sep"></span>Maintain <span class="sep"></span>Remodel
    </p>
  </section>
</main>
</body>
</html>
```